Voltara Solutions Ltd - Project for new electric vehicle charging company

Please use Voltara Solutions Ltd logo & artwork instead of Brimwell.

We would like to produce a leaflet to advertise our electric vehicle charging company to build a reputation and workflow in the local area.

We would like to use the attached logo and maintain the colour palette of the of the logo to be simple, modern and effective.

I have over 15 years experience in the electrical industry and have direct access to the latest technology in electric vehicle charging.

All quotes to remain fixed costs subject to survey of the property and maintenance options can be available.

We can also offer further remedial works to any property through our sister company Brimwell Solutions Ltd.

Target Market(s)

Domestic / commercial customers

Requirements
Must have
• Voltara Solutions Ltd logo and colour palette.
Should not have
• Brimwell logo, Email or website address.

```html
<!DOCTYPE html>
<html lang="en">
<head>
<meta charset="utf-8">
<title>Voltara Solutions Ltd – EV Charging Leaflet</title>
<link rel="stylesheet" href="https://fonts.googleapis.com/css2?family=Montserrat:wght@400;500;600;700;800;900&display=swap">
<style>
  :root {
    --teal: #00b29a;
    --teal-dark: #009c87;
    --ink: #242424;
    --white: #ffffff;
    --lime: #a3cc38;
    --page: #f2f2f2;
  }
  * { margin: 0; padding: 0; box-sizing: border-box; }
  html, body { width: 1200px; height: 2483px; overflow: hidden; }
  body { background: var(--page); font-family: "Montserrat", sans-serif; position: relative; }

  .leaflet {
    position: absolute; left: 100px; top: 596px;
    width: 900px; height: 1163px;
    transform: scale(1.1111); transform-origin: top left;
    background: var(--white);
    box-shadow: 0 10px 30px rgba(0,0,0,0.18);
    overflow: hidden;
  }
  .hero-bg { position: absolute; left: 0; top: 0; width: 900px; height: 592px; }

  .brand { position: absolute; left: 40px; top: 52px; display: flex; align-items: center; gap: 14px; }
  .brand-dot { width: 74px; height: 74px; border-radius: 50%; background: var(--teal); }
  .brand-name { color: var(--teal); font-weight: 500; font-size: 46px; line-height: 1; letter-spacing: 0.5px; }
  .brand-sub { color: var(--teal); font-weight: 500; font-size: 12px; letter-spacing: 9px; margin-top: 6px; }

  .headline { position: absolute; left: 48px; top: 192px; width: 420px; text-transform: uppercase; white-space: nowrap; }
  .headline span { display: block; line-height: 1; }
  .hl-better { font-size: 74px; font-weight: 600; color: var(--ink); letter-spacing: 1px; }
  .hl-way { font-size: 46px; font-weight: 800; color: var(--white); margin-top: 10px; }
  .hl-your { font-size: 48px; font-weight: 800; color: var(--ink); margin-top: 4px; }
  .hl-vehicle { font-size: 54px; font-weight: 800; color: var(--white); letter-spacing: 28px; margin-top: 8px; }
  .hero-rule { position: absolute; left: 48px; top: 444px; width: 414px; height: 3px; background: var(--white); }
  .tagline { position: absolute; left: 46px; top: 473px; font-size: 36px; font-weight: 400; color: var(--ink); line-height: 1.0; }

  .art { position: absolute; }
  .art-charger { left: 505px; top: 90px; width: 395px; height: 495px;
    background: linear-gradient(160deg, #a9d13e 0%, #8fc03a 40%, #c7d4dc 75%, #9aa6ad 100%); opacity: 0.9; border-radius: 8px 0 0 0; }
  .art-car { left: 450px; top: 728px; width: 450px; height: 250px;
    background: linear-gradient(120deg, #8cba37 0%, #f4f6f6 45%, #1f3b5c 100%); opacity: 0.85; border-radius: 6px 0 0 6px; }

  .divider { position: absolute; left: 0; top: 585px; width: 900px; height: 6px; background: var(--ink); }

  .revolution { position: absolute; left: 48px; top: 612px; text-transform: uppercase; line-height: 1; white-space: nowrap; }
  .rev-1 { display: block; color: var(--teal); font-size: 52px; font-weight: 800; }
  .rev-2 { display: block; color: var(--ink); font-size: 41px; font-weight: 800; margin-top: 6px; }

  .experience { position: absolute; left: 475px; top: 626px; width: 365px; font-size: 19.5px; line-height: 1.15; color: var(--ink); }
  .experience strong { color: var(--teal); font-weight: 700; }

  .points { position: absolute; left: 52px; top: 748px; width: 355px; list-style: none; }
  .points li { position: relative; padding-left: 38px; font-size: 19.5px; line-height: 1.15; color: var(--ink); margin-bottom: 25px; }
  .points svg { position: absolute; left: 0; top: 0; width: 23px; height: 23px; }

  .cta { position: absolute; left: 48px; top: 979px; font-size: 37px; font-weight: 800; color: var(--teal); text-transform: uppercase; white-space: nowrap; }

  .footer { position: absolute; left: 0; top: 1038px; width: 900px; height: 100px; background: var(--ink);
    display: flex; align-items: center; padding-left: 56px; gap: 18px; color: var(--white); font-weight: 700; font-size: 17.5px; }
  .footer .item { display: flex; align-items: center; gap: 10px; margin-right: 14px; }
  .footer svg { width: 22px; height: 22px; }
</style>
</head>
<body>
<main class="leaflet">
  <svg class="hero-bg" viewBox="0 0 900 592" aria-hidden="true">
    <rect width="900" height="592" fill="var(--teal)"/>
    <polygon points="0,0 450,0 365,175 0,175" fill="var(--ink)"/>
    <polygon points="438,0 452,0 367,175 353,175" fill="var(--white)" opacity="0.9"/>
  </svg>

  <div class="brand">
    <div class="brand-dot"></div>
    <div>
      <div class="brand-name">Voltara</div>
      <div class="brand-sub">SOLUTIONS LTD</div>
    </div>
  </div>

  <h1 class="headline">
    <span class="hl-better">A Better</span>
    <span class="hl-way">Way to Charge</span>
    <span class="hl-your">Your Electric</span>
    <span class="hl-vehicle">Vehicle</span>
  </h1>
  <div class="hero-rule"></div>
  <p class="tagline">Powering Your Electric<br>Vehicle with Confidence</p>

  <div class="art art-charger" role="img" aria-label="Illustration of a green EV charging station plugged into a silver car"></div>

  <div class="divider"></div>

  <h2 class="revolution">
    <span class="rev-1">Be a part of</span>
    <span class="rev-2">Our Revolution</span>
  </h2>

  <p class="experience">I have over <strong>15 years experience</strong> in the electrical industry and have direct access to the latest technology in electric vehicle charging.</p>

  <ul class="points">
    <li>
      <svg viewBox="0 0 24 24"><circle cx="12" cy="12" r="12" fill="var(--teal)"/><path d="M6.5 12.5l3.5 3.5 7.5-7.5" fill="none" stroke="#fff" stroke-width="2.6" stroke-linecap="round" stroke-linejoin="round"/></svg>
      All quotes to remain fixed costs subject to survey of the property and maintenance options can be available.
    </li>
    <li>
      <svg viewBox="0 0 24 24"><circle cx="12" cy="12" r="12" fill="var(--teal)"/><path d="M6.5 12.5l3.5 3.5 7.5-7.5" fill="none" stroke="#fff" stroke-width="2.6" stroke-linecap="round" stroke-linejoin="round"/></svg>
      We can also offer further remedial works to any property through our sister company Brimwell Solutions Ltd.
    </li>
  </ul>

  <div class="art art-car" role="img" aria-label="Illustration of a white electric car charging at a green roadside charger"></div>

  <p class="cta">Contact us for working with you</p>

  <footer class="footer">
    <span class="item">
      <svg viewBox="0 0 24 24"><path d="M6.6 10.8a15 15 0 0 0 6.6 6.6l2.2-2.2a1 1 0 0 1 1-.25 11.4 11.4 0 0 0 3.6.57 1 1 0 0 1 1 1V20a1 1 0 0 1-1 1A17 17 0 0 1 3 4a1 1 0 0 1 1-1h3.5a1 1 0 0 1 1 1c0 1.25.2 2.45.57 3.57a1 1 0 0 1-.25 1z" fill="var(--teal)"/></svg>
      5550-187-3926
    </span>
    <span class="item">
      <svg viewBox="0 0 24 24"><rect x="2" y="5" width="20" height="14" rx="1.5" fill="var(--teal)"/><path d="M3 6l9 7 9-7" fill="none" stroke="var(--ink)" stroke-width="1.6"/></svg>
      info@voltaracharge.com
    </span>
    <span class="item">
      <svg viewBox="0 0 24 24"><circle cx="12" cy="12" r="9.5" fill="none" stroke="var(--teal)" stroke-width="2"/><ellipse cx="12" cy="12" rx="4" ry="9.5" fill="none" stroke="var(--teal)" stroke-width="1.6"/><path d="M2.5 12h19M4 7h16M4 17h16" stroke="var(--teal)" stroke-width="1.4"/></svg>
      www.voltaracharge.com
    </span>
  </footer>
</main>
</body>
</html>
```